Business Intelligence Dashboard header

We are a top 10 cancer treatment clinic. Our analytics teams (Corporate Finance, Financial Analytics, and Clinical Analytics) are searching for a great graphic to show our business partners the value of our business intelligence products. We are hoping to convey that we are tech-savvy, supportive to our patients and mission of saving lives, valuable, forward-thinking, agile, supportive, and friendly.

This header will be placed at the top of each data visualization ('viz') that we create. We would like a design that is in-line with our company branding, simple, elegant, and striking. We primarily create headers that are between 800 and 1300 pixels across (800 and 1300 being the most common) and between 60 and 80 pixels high (76 being our current header height in px, but we are open to slight deviation.) The type of data visualizations this will sit atop (everything we produce, but just a few examples) will be things like patient safety, clinic utilization, appointment volumes, provider scorecards, and many more. I've included our current header, and a header I saw and liked (although I think it could have been a bit cooler.)

I'm open to ideas, feedback, and your opinion as a designer to come up with something amazing. You can find our website at https://www.brightharborhealth.org/
Googling our business shows our main clinic (with the rounded front) https://www.findwell.com/search?q=brightharbor+oncology+partners&source=lnms&tbm=isch&sa=X&ved=0ahUKEwjjws22xuLXAhVM5mMKHb82CpQQ_AUIDCgD&biw=1995&bih=916

We are open to stock images.

Requirements
Must have
• A place to write in a dashboard title (we will use our own BI-native object to float over the top of this banner)
Nice to have
• We would like a place/icon to differentiate between work products coming out of Clinical Analytics/Financial Analytics/Corporate Finance. We're fine with it being on 2 lines, or simply designing an icon to differentiate. We could use smaller text underneath the dashboard title (see must haves), an icon for each of the 3 teams, or a space in the header to write in the team ourselves. The team names should be of limited significance on the header. The star of the show will be the dashboard title (just leave an area for it) where the team names should be of less significance (off to the side, under the title in smaller font, etc)

```html
<!DOCTYPE html>
<html lang="en">
<head>
<meta charset="utf-8">
<title>Dashboard Header Options</title>
<link href="https://fonts.googleapis.com/css2?family=Open+Sans:wght@400;600;700&display=swap" rel="stylesheet">
<style>
  :root {
    --page-bg: #121212;
    --label: #f2b51b;
    --slate: #6e6766;
    --slate-dark: #57514f;
    --gold: #ffc622;
    --amber: #f2a416;
    --rust: #b45c0a;
    --title-brown: #7b4300;
    --white: #ffffff;
  }
  * { box-sizing: border-box; margin: 0; padding: 0; }
  html, body {
    width: 1200px; height: 573px; overflow: hidden;
    background: var(--page-bg);
    font-family: "Open Sans", Arial, sans-serif;
  }
  .board { position: relative; width: 1200px; height: 573px; }
  .version-label {
    position: absolute; left: 124px;
    font-size: 12px; color: var(--label); font-weight: 400;
  }
  .header-bar {
    position: absolute; left: 80px; width: 1040px; height: 63px;
    background: var(--gold); overflow: hidden;
  }
  .header-bar.has-base { height: 64px; border-bottom: 4px solid var(--slate-dark); }
  .stock-visual {
    position: absolute; top: 0; bottom: 0; left: 470px; right: 0;
    background: linear-gradient(90deg, rgba(255,198,34,0) 0%, #eaa91c 30%, #d18a12 60%, var(--rust) 88%);
  }
  .brand-panel {
    position: absolute; top: 0; left: 0; bottom: 0;
    background: var(--slate);
  }
  .brand-name {
    position: absolute; top: 50%; transform: translateY(-50%);
    color: var(--white); font-weight: 700; font-size: 12px; line-height: 14px;
    white-space: nowrap;
  }
  .dashboard-title {
    position: absolute; left: 176px; top: 50%; transform: translateY(-50%);
    font-size: 29px; font-weight: 700; color: var(--title-brown); letter-spacing: -0.2px;
    white-space: nowrap;
  }
  .team-tag {
    position: absolute; right: 16px; top: 50%; transform: translateY(-50%);
    display: flex; align-items: center; gap: 8px;
  }
  .team-icon { width: 24px; height: 24px; }
  .team-name { color: var(--white); font-size: 14px; line-height: 14.5px; font-weight: 400; }

  /* V1: curved edge */
  .v1 .brand-panel { width: 140px; }
  .v1 .curve-rim, .v1 .curve-fill {
    position: absolute; top: 0; bottom: 0; right: 0;
    border-top-left-radius: 44px 63px;
  }
  .v1 .curve-rim { left: 112px; background: var(--amber); }
  .v1 .curve-fill { left: 118px; background: var(--gold); }

  /* V2: straight edge with accent stripe */
  .v2 .brand-panel { width: 142px; }
  .v2 .accent-stripe {
    position: absolute; top: 0; bottom: 0; left: 142px; width: 10px; background: var(--amber);
  }

  /* V3: chevron edge */
  .v3 .chevron { position: absolute; top: 0; left: 0; height: 100%; }
</style>
</head>
<body>
<main class="board">

  <span class="version-label" style="top:81px">V1</span>
  <section class="header-bar v1" style="top:110px">
    <div class="brand-panel"></div>
    <div class="curve-rim"></div>
    <div class="curve-fill"></div>
    <div class="stock-visual" role="img" aria-label="Golden DNA double helix stock image fading into the banner"></div>
    <div class="brand-name" style="left:20px">Bright Harbor<br>Health</div>
    <h1 class="dashboard-title">Your Dashboard Title</h1>
    <div class="team-tag">
      <svg class="team-icon" viewBox="0 0 24 24" aria-hidden="true">
        <circle cx="12" cy="12" r="12" fill="var(--gold)"/>
        <polyline points="3,13 8,13 10,8 13,17 15,11 16,13 21,13" fill="none" stroke="var(--rust)" stroke-width="1.8" stroke-linejoin="round" stroke-linecap="round"/>
      </svg>
      <span class="team-name">Clinical<br>Analytics</span>
    </div>
  </section>

  <span class="version-label" style="top:226px">V2</span>
  <section class="header-bar v2 has-base" style="top:254px">
    <div class="stock-visual" role="img" aria-label="Golden line chart with data points stock image fading into the banner"></div>
    <div class="brand-panel"></div>
    <div class="accent-stripe"></div>
    <div class="brand-name" style="left:28px">Bright Harbor<br>Health</div>
    <h1 class="dashboard-title">Your Dashboard Title</h1>
    <div class="team-tag">
      <svg class="team-icon" viewBox="0 0 24 24" aria-hidden="true">
        <circle cx="12" cy="12" r="12" fill="var(--gold)"/>
        <rect x="6" y="11" width="3" height="8" fill="var(--rust)"/>
        <rect x="10.5" y="6" width="3" height="13" fill="var(--rust)"/>
        <rect x="15" y="13" width="3" height="6" fill="var(--rust)"/>
      </svg>
      <span class="team-name">Corporate<br>Finance</span>
    </div>
  </section>

  <span class="version-label" style="top:372px">V3</span>
  <section class="header-bar v3 has-base" style="top:401px">
    <div class="stock-visual" role="img" aria-label="Golden digital wireframe stock image fading into the banner"></div>
    <svg class="chevron" width="160" height="60" viewBox="0 0 160 60" preserveAspectRatio="none" aria-hidden="true">
      <polygon points="0,0 128,0 152,30 128,60 0,60" fill="var(--amber)"/>
      <polygon points="0,0 120,0 144,30 120,60 0,60" fill="var(--slate)"/>
    </svg>
    <div class="brand-name" style="left:28px">Bright Harbor<br>Health</div>
    <h1 class="dashboard-title">Your Dashboard Title</h1>
    <div class="team-tag">
      <svg class="team-icon" viewBox="0 0 24 24" aria-hidden="true">
        <circle cx="12" cy="12" r="12" fill="var(--gold)"/>
        <polyline points="5,17 9,11 13,14 19,7" fill="none" stroke="var(--rust)" stroke-width="2.2" stroke-linejoin="round" stroke-linecap="round"/>
        <circle cx="19" cy="7" r="1.8" fill="var(--rust)"/>
      </svg>
      <span class="team-name">Financial<br>Analytics</span>
    </div>
  </section>

</main>
</body>
</html>
```